Exercise Physiologist needs a Brochure

I am Exercise Physiologist providing exercise therapy for a variety of conditions. I have a logo and recent business card design. I like the black background like the front of the business cards. I have attached the flyer information required. I have also attached a few photos however they do not have to be used, happy to have no photos at all.

Industry/Entity Type

Health And Wellness

Font styles to use
Sans Serif

Requirements
Must have
• Please also add instagram @varnolhealth
Nice to have
• tri-fold brochure

```html
<!DOCTYPE html>
<html lang="en">
<head>
<meta charset="utf-8">
<title>Varnol Health &amp; Rehabilitation – Exercise Physiology Flyer</title>
<link href="https://fonts.googleapis.com/css2?family=Arimo:wght@400;700&family=Mulish:wght@400;600;700;800;900&display=swap" rel="stylesheet">
<style>
  :root {
    --brand-blue: #2459a8;
    --sky-blue: #3a9ad9;
    --name-blue: #4aa8e0;
    --ink: #222;
    --black-band: #1d1d1f;
    --dash-grey: #9a9a9a;
    --white: #fff;
  }
  * { box-sizing: border-box; margin: 0; padding: 0; }
  html, body { width: 904px; height: 1200px; overflow: hidden; background: var(--white); }
  body { position: relative; font-family: "Mulish", Arial, sans-serif; color: var(--ink); }
  .abs { position: absolute; }

  /* brand */
  .brand { left: 38px; top: 40px; display: flex; align-items: center; gap: 14px; }
  .brand-dot { width: 88px; height: 88px; border-radius: 50%; background: var(--sky-blue); border: 6px solid var(--brand-blue); }
  .brand-name { font-weight: 700; font-size: 64px; color: var(--brand-blue); letter-spacing: -1px; }

  /* credentials panel */
  .credentials {
    left: 417px; top: 23px; width: 487px; height: 136px;
    background: var(--black-band); border-radius: 22px 0 0 22px;
    color: var(--white); text-align: center; padding-top: 8px;
  }
  .credentials .name { font-weight: 800; font-size: 30px; color: var(--name-blue); line-height: 34px; }
  .credentials .role { font-weight: 400; font-size: 22px; line-height: 28px; margin-top: 4px; }
  .credentials .quals { font-weight: 400; font-size: 14px; line-height: 18px; }

  /* headline */
  .headline { left: 0; width: 904px; top: 203px; text-align: center; font-weight: 800; font-size: 26px; color: var(--brand-blue); }
  .headline-rule { left: 418px; top: 246px; width: 68px; height: 2px; background: var(--brand-blue); }

  .intro-pill {
    left: 33px; top: 257px; width: 838px; height: 78px; border-radius: 40px;
    background: linear-gradient(#f4f4f4, #e8e8e8); box-shadow: 0 10px 10px -8px rgba(0,0,0,.15);
    text-align: center; font-weight: 400; font-size: 20px; line-height: 27px; padding-top: 11px; color: #2a2a2a;
  }

  /* section headers */
  .section-rule { height: 2px; background: var(--brand-blue); }
  .section-pill {
    height: 31px; border-radius: 16px; background: var(--brand-blue); color: var(--white);
    font-weight: 900; font-size: 20px; line-height: 31px; text-align: center;
  }

  .about-text { left: 36px; top: 419px; width: 832px; text-align: center; font-family: "Arimo", Arial, sans-serif; font-size: 15.5px; line-height: 20px; }

  .help-box {
    left: 37px; top: 533px; width: 830px; height: 218px;
    border: 1.5px dashed var(--dash-grey); border-radius: 18px; background: #f1f1f1;
    padding: 29px 28px 0 28px; font-weight: 400; font-size: 16px; line-height: 22px; text-align: justify;
  }
  .help-box p + p { margin-top: 8px; }

  /* conditions */
  .conditions { list-style: none; font-weight: 700; font-size: 19px; color: var(--sky-blue); }
  .conditions li { position: absolute; white-space: nowrap; line-height: 24px; }
  .conditions li::before {
    content: ""; position: absolute; left: -32px; top: 7px; width: 10px; height: 10px; border-radius: 50%; background: var(--brand-blue);
  }

  .closing { left: 30px; width: 844px; top: 1003px; text-align: center; font-weight: 800; font-size: 16.8px; line-height: 23px; color: var(--brand-blue); }

  /* footer */
  .footer { left: 0; top: 1083px; width: 904px; height: 117px; background: var(--black-band); border-top: 4px solid var(--brand-blue); }
  .contact { color: var(--white); display: flex; align-items: center; gap: 10px; font-weight: 400; font-size: 16px; }
  .contact svg { width: 18px; height: 18px; flex: none; }
  .contact.phone { font-weight: 900; font-size: 25px; }
  .contact .venue { color: var(--name-blue); margin-left: 6px; }
</style>
</head>
<body>
  <div class="abs brand">
    <div class="brand-dot"></div>
    <div class="brand-name">varnol</div>
  </div>

  <div class="abs credentials">
    <div class="name">CLAIRE DUNMORE</div>
    <div class="role">Exercise Physiologist</div>
    <div class="quals">B.AppSci – Human Mvmt</div>
    <div class="quals">Grad Dip – ExRehab</div>
    <div class="quals">Cert IV – Training &amp; Assessment</div>
  </div>

  <h1 class="abs headline">HEAL THROUGH MOVEMENT</h1>
  <div class="abs headline-rule"></div>

  <div class="abs intro-pill">
    Don’t let the right exercise but the wrong technique hinder your recovery<br>
    Discover how important the correct exercise technique is to your success
  </div>

  <div class="abs section-rule" style="left:142px;top:385px;width:620px"></div>
  <h2 class="abs section-pill" style="left:189px;top:370px;width:527px">WHAT IS AN EXERCISE PHYSIOLOGIST?</h2>
  <p class="abs about-text">Exercise Physiologists are university educated health professionals trained to provide exercise therapy for pain and injury, pre and post surgery, mental health and chronic disease. They are registered providers with RoadCover, SafeWork Board, PublicCare and the Veterans Services Office and many Private Health funds</p>

  <div class="abs help-box">
    <p>I have over 13 years of experience working as an Exercise Physiologist and have been working in the sport and fitness industry since 1996. I understand that everyone’s health and exercise experience is unique and will tailor a program to suit you and your lifestyle.</p>
    <p>Managing your condition involves working with you to develop the best exercises and teaching you the correct technique essential to improve. Home and gym based programs can be provided.</p>
    <p>When appropriate I can also work with your current treating health practitioner to provide a holistic approach to your recovery.</p>
  </div>
  <h2 class="abs section-pill" style="left:271px;top:517px;width:362px">HOW CAN I HELP YOU?</h2>

  <div class="abs section-rule" style="left:77px;top:779px;width:750px"></div>
  <h2 class="abs section-pill" style="left:109px;top:763px;width:685px">COMMON CONDITIONS THAT BENEFIT FROM EXERCISE</h2>

  <ul class="conditions">
    <li style="left:128px;top:823px">Back pain</li>
    <li style="left:128px;top:853px">Joint pain</li>
    <li style="left:128px;top:883px">Pain relating to exercise</li>
    <li style="left:128px;top:913px">Arthritis</li>
    <li style="left:128px;top:947px">Anxiety relating to exercise</li>
    <li style="left:483px;top:823px">Depression and Anxiety</li>
    <li style="left:483px;top:857px">Chronic diseases such as diabetes,<br>heart and lung disease.</li>
    <li style="left:483px;top:915px">Motor vehicle accidents</li>
  </ul>

  <p class="abs closing">Performing the right exercise the wrong way can do more harm than good. I can teach you what, how and when to perform your tailored exercise program to get the best results.</p>

  <footer class="abs footer"></footer>
  <h2 class="abs section-pill" style="left:109px;top:1066px;width:685px;font-size:21px">CALL OR EMAIL ME TODAY TO SEE HOW I CAN HELP</h2>

  <div class="abs contact phone" style="left:36px;top:1106px">
    <svg viewBox="0 0 20 20"><circle cx="10" cy="10" r="10" fill="#4aa8e0"/><path d="M7 5l2 3-1.2 1.2a7 7 0 0 0 3 3L12 11l3 2-1 2c-4 0-8-4-8-8z" fill="#1d1d1f"/></svg>
    <span>0400 555 182</span>
  </div>
  <div class="abs contact" style="left:36px;top:1137px">
    <svg viewBox="0 0 20 20"><circle cx="10" cy="10" r="10" fill="#4aa8e0"/><path d="M10 4a4 4 0 0 0-4 4c0 3 4 8 4 8s4-5 4-8a4 4 0 0 0-4-4zm0 5.6a1.6 1.6 0 1 1 0-3.2 1.6 1.6 0 0 1 0 3.2z" fill="#1d1d1f"/></svg>
    <span>Gate 2, 14 Ridgeline Rd NORTH BANFIELD<span class="venue">(Hartwell Fitness)</span></span>
  </div>
  <div class="abs contact" style="left:36px;top:1162px">
    <svg viewBox="0 0 20 20"><circle cx="10" cy="10" r="10" fill="#4aa8e0"/><rect x="5" y="6.5" width="10" height="7" fill="#1d1d1f"/><path d="M5 6.5l5 4 5-4" stroke="#4aa8e0" fill="none"/></svg>
    <span>varnolhealth@mailbox.com</span>
  </div>
  <div class="abs contact" style="left:658px;top:1137px">
    <svg viewBox="0 0 20 20"><circle cx="10" cy="10" r="10" fill="#4aa8e0"/><g fill="none" stroke="#1d1d1f" stroke-width="1.8" stroke-linecap="round"><path d="M9 11.5l-1.2 1.2a2 2 0 0 1-2.8-2.8l1.6-1.6a2 2 0 0 1 2.8 0"/><path d="M11 8.5l1.2-1.2a2 2 0 0 1 2.8 2.8l-1.6 1.6a2 2 0 0 1-2.8 0"/></g></svg>
    <span>social.page/Varnol</span>
  </div>
  <div class="abs contact" style="left:658px;top:1162px">
    <svg viewBox="0 0 20 20"><circle cx="10" cy="10" r="10" fill="#4aa8e0"/><path d="M5.5 6.5h9v5.5h-5l-2.5 2v-2h-1.5z" fill="#1d1d1f"/></svg>
    <span>@varnolhealth</span>
  </div>
</body>
</html>
```